Lotus Leaf Kitchen Road Billboard

Road Billboard I need all of this information on it
Authentic Thai Food Bangkok Style
6.5 Miles on the right
4126 Maple Ridge Rd Otto NC
828-555-4172

```html
<!DOCTYPE html>
<html lang="en">
<head>
<meta charset="utf-8">
<title>Lotus Leaf Kitchen – Road Billboard</title>
<link href="https://fonts.googleapis.com/css2?family=Bowlby+One&family=Dancing+Script:wght@700&family=Poppins:wght@400;600;700;800&family=Yellowtail&display=block" rel="stylesheet">
<style>
  :root {
    --stage: #666666;
    --night: #0d0c0c;
    --gold: #e2ac1e;
    --white: #ffffff;
    --arrow: #ff6a0a;
  }
  html, body {
    margin: 0;
    width: 1200px;
    height: 707px;
    overflow: hidden;
    background: var(--stage);
  }
  .billboard {
    position: absolute;
    left: 96px;
    top: 102px;
    width: 1008px;
    height: 504px;
    overflow: hidden;
    background:
      radial-gradient(ellipse 340px 300px at 120px 260px, rgba(120, 40, 10, .55), transparent 70%),
      linear-gradient(180deg, #161312 0%, var(--night) 100%);
    font-family: "Poppins", sans-serif;
  }
  .hero-photo {
    position: absolute;
    left: 464px;
    top: 98px;
    width: 544px;
    height: 406px;
    background:
      radial-gradient(ellipse 180px 120px at 230px 150px, rgba(120, 150, 80, .55), transparent 70%),
      radial-gradient(ellipse 300px 140px at 260px 250px, rgba(70, 66, 62, .9), transparent 75%),
      radial-gradient(ellipse 170px 110px at 90px 200px, rgba(240, 138, 28, .75), transparent 70%),
      radial-gradient(ellipse 150px 90px at 440px 370px, rgba(240, 138, 28, .7), transparent 70%),
      linear-gradient(180deg, rgba(13, 12, 12, 0) 0%, var(--night) 100%);
  }
  .headline-top {
    position: absolute;
    left: 40px;
    top: 50px;
    margin: 0;
    font-family: "Bowlby One", sans-serif;
    font-weight: 400;
    font-size: 74px;
    line-height: 1;
    color: var(--gold);
    letter-spacing: 1px;
    white-space: nowrap;
  }
  .headline-main {
    position: absolute;
    left: 38px;
    top: 118px;
    margin: 0;
    font-weight: 800;
    font-size: 90px;
    line-height: 1;
    color: var(--white);
    letter-spacing: -1px;
    white-space: nowrap;
  }
  .headline-script {
    position: absolute;
    left: 92px;
    top: 200px;
    margin: 0;
    font-family: "Yellowtail", "Dancing Script", cursive;
    font-weight: 400;
    font-size: 64px;
    line-height: 1;
    color: var(--gold);
    white-space: nowrap;
  }
  .direction-arrow {
    position: absolute;
    left: 85px;
    top: 282px;
    width: 448px;
    height: 52px;
    overflow: visible;
  }
  .direction-text {
    position: absolute;
    left: 97px;
    top: 284px;
    margin: 0;
    font-weight: 600;
    font-size: 31px;
    line-height: 44px;
    color: var(--white);
    white-space: nowrap;
  }
  .address {
    position: absolute;
    left: 80px;
    top: 336px;
    margin: 0;
    display: flex;
    align-items: center;
    gap: 14px;
    font-weight: 400;
    font-size: 29px;
    line-height: 40px;
    color: var(--white);
    white-space: nowrap;
  }
  .address svg { width: 20px; height: 22px; }
  .phone {
    position: absolute;
    left: 80px;
    top: 392px;
    margin: 0;
    font-weight: 700;
    font-size: 62px;
    line-height: 1;
    color: var(--gold);
    letter-spacing: 1px;
    white-space: nowrap;
  }
  .brand-name {
    position: absolute;
    left: 770px;
    top: 144px;
    width: 220px;
    margin: 0;
    text-align: center;
    font-weight: 600;
    font-size: 21px;
    line-height: 1.2;
    color: var(--gold);
    white-space: nowrap;
  }
</style>
</head>
<body>
  <main class="billboard">
    <div class="hero-photo" role="img" aria-label="Flaming wok with shrimp, broccoli and vegetables tossed in the air over fire"></div>

    <h1 class="headline-top">AUTHENTIC</h1>
    <p class="headline-main">THAI FOOD</p>
    <p class="headline-script">Bangkok Style</p>

    <svg class="direction-arrow" viewBox="0 0 448 52" aria-hidden="true">
      <polygon points="0,4 388,4 388,-6 448,26 388,58 388,48 0,48" fill="var(--arrow)"/>
    </svg>
    <p class="direction-text">6.5 Miles on the right</p>

    <p class="address">
      <svg viewBox="0 0 20 22" aria-hidden="true">
        <path d="M10 1a7 7 0 0 0-7 7c0 5 7 12 7 12s7-7 7-12a7 7 0 0 0-7-7zm0 9.5a2.5 2.5 0 1 1 0-5 2.5 2.5 0 0 1 0 5z" fill="var(--gold)"/>
      </svg>
      4126 Maple Ridge Rd Otto NC
    </p>

    <p class="phone">828-555-4172</p>

    <p class="brand-name">Lotus Leaf Kitchen</p>
  </main>
</body>
</html>
```